Designer Furniture: Brochure Design | Price List | Price Cards

1. brochure 2. price list 3. showroom price cards

We need a brochure design of our high-end wood and acrylic furniture line. We are a custom plastics & acrylics manufacturing company - one facet of our business is custom high-end furniture. We have developed our own proprietary designer furniture line and need a brochure and supporting price list and showroom price cards to reflect the furniture's unique wood and acrylic high-end design appeal.

****More supporting informational & graphic files at:****
https://www.filecrate-share.com/sh/qvbrumtxpkaow7e/pLemRtZdKw

We would like to see the following design style: European, modern, clean lines | Lots of white | warm greys | minimalistic in "graphic design" to show off our "furniture design" as the primary focus of the brochure "less is more" | we work in the high-end design market so our look and feel has to reflect that of 'design' | a screenshot of an example of what we like is included in supplied files | we like modern artwork

This is a North American print distribution. Further detailed instructions & details are supplied in the supporting uploaded files of the project.

The winning design may lead to future exclusive design work in this particular facet of our business - possibly others.

* Price list: should be editable PDF (printed on in-house monochrome laser) that is a secondary insert in to the brochure - B&W 6.75"x8.25" Portrait. Includes each item in table or catalogue-type format with dimensions and pricing "$###.##"

* Showroom price card: editable PDF file for each piece of furniture. 5"x7" Portrait OR Landscape. Should include the main 2D dimensional line drawing of each piece along with dimensions and Brookvale Logo or Icon and QRCode from OLD brochure design.
Updates

*****Supporting files & graphic files at:******

- It is imperative that all 3D renderings from our "Rendering" folder in dropbox link be shown in our brochure.

- The price list is a monochrome listing of all our pieces of furniture with dimensions and prices in a table or catalogue-type format.

Here's to clear up some of the questions you've been asking:

PRICE CARDS:
5"x7" portrait
These cards will be but in to an acrylic stand and sit on each piece of furniture - so would probably be best to design a front and back.
Side #1 with specifics: Product name, product number, dimensions, line drawing, price, Brookvale Logo, QR Code, Contact info
Side #2 the other showcasing 3D image, Product Name, Brookvale logo

PRICE SHEET INSERT:
This is an insert for the brochure cataloguing each of the products, 2D dimensional line drawing, dimensions, product name, product number, price - editable PDF so we can easily change prices and print on our in-house monochrome (black & white) printer. 1 or 2 sided - doesn't matter.  Will fit inside the brochure, so cannot be any larger than 7x8.5 - I would suggest to make .25" smaller than brochure folded size - 6.75x8.25

Target Market(s)

Designers, Architects and High-end Retail Furniture Outlets

Industry/Entity Type

Business

Requirements
Must have
• - Brochure finished folded size must be: 7”w x 8.5”h (PORTRAIT)
- raw print stock is 12.5”x19” – maximum print area is 12”x18.5”
- as long as finished folded size is exactly 7”x8.5” portrait - folding style is up to designer (bifold, 3-panel roll, 4-panel roll)
- Will be digitally printed - RGB on 80lb gloss text
- 3D Render image of each product in the furniture line must be included...see below

****More supporting files & graphic files at:****
Nice to have
• ****Supporting files & graphic files at:****

```html
<!DOCTYPE html>
<html lang="en">
<head>
<meta charset="utf-8">
<title>Brookvale Collection Brochure Spread</title>
<link href="https://fonts.googleapis.com/css2?family=Questrial&display=swap" rel="stylesheet">
<style>
  :root {
    --stage: #e8e8e8;
    --paper: #ffffff;
    --paper-shade: #f3f3f3;
    --title-grey: #8e8e8e;
    --text-grey: #9a9a9a;
    --ink: #1a1a1a;
    --wood-light: #c9b394;
    --wood-mid: #a88f6e;
    --acrylic: #e2e6e8;
  }
  * { margin: 0; padding: 0; box-sizing: border-box; }
  html, body {
    width: 1200px; height: 539px; overflow: hidden;
    background: var(--stage);
    font-family: "Questrial", "Century Gothic", sans-serif;
  }
  .spread {
    position: absolute; left: 160px; top: 60px;
    width: 881px; height: 429px;
    display: flex;
    box-shadow: 0 8px 24px rgba(0,0,0,0.12);
  }
  .panel {
    position: relative; height: 100%;
    background: linear-gradient(90deg, var(--paper) 0%, var(--paper) 70%, var(--paper-shade) 100%);
  }
  .panel--product { width: 353px; padding: 26px 0 0 25px; }
  .panel--flap { width: 175px; background: linear-gradient(90deg, var(--paper-shade) 0%, var(--paper) 20%); }
  .product-title {
    font-size: 36px; font-weight: 400; color: var(--title-grey);
    letter-spacing: 0.5px; line-height: 1;
  }
  .product-spec {
    margin-top: 16px; font-size: 10px; color: var(--text-grey); letter-spacing: 0.3px;
  }
  .product-copy {
    margin-top: 12px; width: 150px; font-size: 8.6px; line-height: 1.25; color: var(--text-grey);
  }
  .product-copy p + p { margin-top: 9px; }
  .product-render {
    position: absolute; left: 25px; top: 220px; width: 300px; height: 185px;
  }
  .flap-copy {
    position: absolute; left: 17px; top: 176px; width: 150px;
    font-size: 7.3px; line-height: 1.3; color: var(--text-grey);
  }
  .flap-copy p + p { margin-top: 8px; }
  .collection-name {
    position: absolute; left: 15px; top: 330px;
    font-size: 30px; color: var(--ink); letter-spacing: 0.5px;
  }
  .maker {
    position: absolute; left: 15px; top: 380px;
    display: flex; align-items: center; gap: 6px;
  }
  .maker-square { width: 30px; height: 30px; background: var(--ink); }
  .maker-name { font-size: 16px; color: var(--ink); line-height: 1; }
  .maker-tag { font-size: 5.5px; color: var(--ink); letter-spacing: 0.6px; margin-top: 2px; }
</style>
</head>
<body>
  <main class="spread">
    <section class="panel panel--product">
      <h1 class="product-title">Tolvana</h1>
      <div class="product-spec">B-BEN100 &nbsp;48″W x 18″H x 12″D</div>
      <div class="product-copy">
        <p>Beatle-Killed Pine Beam nested within clear acrylic legs.</p>
        <p>The wood is polished gently to reveal tha natural beauty of each blue-stained piece of wood and is then finished with tung oil.</p>
      </div>
      <svg class="product-render" viewBox="0 0 300 185" role="img" aria-label="3D render of the Tolvana bench: pine beam nested within two clear acrylic legs">
        <defs>
          <linearGradient id="woodA" x1="0" y1="0" x2="1" y2="1">
            <stop offset="0" stop-color="#d2bd9c"/><stop offset="1" stop-color="#a88f6e"/>
          </linearGradient>
        </defs>
        <rect x="0" y="0" width="300" height="185" fill="url(#woodA)" opacity="0.35"/>
      </svg>
    </section>

    <section class="panel panel--product">
      <h1 class="product-title">Merevine</h1>
      <div class="product-spec">B-BEN110 &nbsp;48″W x 18″H x 12″D</div>
      <div class="product-copy">
        <p>Beatle-Killed Pine Beam seated over clear acrylic legs.</p>
        <p>The wood is polished gently to reveal tha natural beauty of each blue-stained piece of wood and is then finished with tung oil.</p>
      </div>
      <svg class="product-render" viewBox="0 0 300 185" role="img" aria-label="3D render of the Merevine bench: blue-stained pine beam seated over two clear acrylic legs">
        <defs>
          <linearGradient id="woodB" x1="0" y1="0" x2="1" y2="1">
            <stop offset="0" stop-color="#8f7a5f"/><stop offset="1" stop-color="#c7b699"/>
          </linearGradient>
        </defs>
        <rect x="0" y="0" width="300" height="185" fill="url(#woodB)" opacity="0.35"/>
      </svg>
    </section>

    <aside class="panel panel--flap">
      <div class="flap-copy">
        <p>The Brookvale collection is a tribute to the 800 million cubic metres of Lodgepole Pine that have been killed by the Mountain Pine Beetle (MPB) in the Interior of British Columbia.</p>
        <p>The pieces are named using words from Chinook Jargon.</p>
        <p>Chinook Jargon was the unifying trade language of the Pacific Northwest during the 19th century. It was the working language in many of the towns and communities in British Columbia that have been most impacted by the devastation of the Mountain Pine Beetle.</p>
      </div>
      <div class="collection-name">Brookvale</div>
      <div class="maker">
        <div class="maker-square"></div>
        <div>
          <div class="maker-name">HARROWGATE</div>
          <div class="maker-tag">CUSTOM PLASTICS &amp; ACRYLICS</div>
        </div>
      </div>
    </aside>
  </main>
</body>
</html>
```